Hedge fund needs power point design for marketing pitch

We need a designer to make our power point pitch more aesthetically appealing to potential clients. We will be marketing our hedge fund to high net worth individuals and financial institutions. The ideal design will look professional and project confidence to our potential clients. We have attached a rough outline of what we have completed so far. We have also attached example cover pages for 2 pitch books produced by our competitors.

Target Market(s)

Financial institutions and wealthy investors

Industry/Entity Type

Finance

Requirements
Must have
• must use our logo and current slides. Must look professional

```html
<!DOCTYPE html>
<html lang="en">
<head>
<meta charset="utf-8">
<title>Investment Objective</title>
<link rel="stylesheet" href="https://fonts.googleapis.com/css2?family=Carlito:wght@400;700&display=swap">
<style>
  :root {
    --sky-top: #e9e9e7;
    --sky-mid: #dcdddb;
    --spray: #c9d2d4;
    --foam-green: #a9b94a;
    --sea-dark: #2c2b28;
    --sea-mid: #4a4a46;
    --title-blue: #17a8e8;
    --panel-fill: #7736a8;
    --panel-edge: #5a2584;
    --panel-light: #9a5cc8;
    --text-white: #ffffff;
  }
  * { margin: 0; padding: 0; box-sizing: border-box; }
  html, body { width: 1200px; height: 900px; overflow: hidden; }
  body { font-family: "Carlito", "Calibri", sans-serif; background: var(--sky-top); }

  .slide { position: relative; width: 1200px; height: 900px; overflow: hidden; }

  .backdrop {
    position: absolute; inset: 0;
    background:
      radial-gradient(ellipse 260px 420px at 560px 380px, rgba(255,255,255,0.75), rgba(255,255,255,0) 70%),
      radial-gradient(ellipse 180px 160px at 1150px 560px, rgba(169,185,74,0.55), rgba(169,185,74,0) 75%),
      radial-gradient(ellipse 140px 200px at 680px 420px, rgba(169,185,74,0.45), rgba(169,185,74,0) 75%),
      linear-gradient(to bottom,
        var(--sky-top) 0%,
        var(--sky-mid) 45%,
        var(--spray) 62%,
        var(--sea-mid) 80%,
        var(--sea-dark) 84%,
        var(--sea-mid) 92%,
        #6b6b66 100%);
  }

  .slide-title {
    position: absolute; left: 0; right: 0; top: 168px;
    text-align: center;
    font-weight: 700; font-size: 64px; line-height: 1;
    color: var(--title-blue);
  }

  .panels { position: absolute; left: 0; top: 0; width: 1200px; height: 900px; }

  .panel-text {
    position: absolute;
    color: var(--text-white);
    font-size: 28px; line-height: 40px;
    list-style: none;
  }
  .panel-text li { position: relative; padding-left: 44px; }
  .panel-text li::before {
    content: ""; position: absolute; left: 0; top: 15px;
    width: 9px; height: 9px; background: var(--text-white);
  }
  .panel-text .sub-list { list-style: none; margin-top: 4px; }
  .panel-text .sub-list li { padding-left: 52px; margin-left: 8px; margin-bottom: 8px; }
  .panel-text .sub-list li::before {
    width: 20px; height: 2px; top: 20px; left: 8px;
  }
  .objective-left { left: 134px; top: 348px; width: 420px; }
  .objective-right { left: 638px; top: 352px; width: 420px; }
</style>
</head>
<body>
<main class="slide">
  <div class="backdrop" role="img" aria-label="Photograph of a large ocean wave crashing against a sea wall under a pale grey sky"></div>

  <h1 class="slide-title">Investment Objective</h1>

  <svg class="panels" viewBox="0 0 1200 900" aria-hidden="true">
    <polygon points="116,300 566,300 592,326 592,721 160,721 112,672 112,304"
             fill="var(--panel-fill)" stroke="var(--panel-edge)" stroke-width="5"/>
    <polyline points="116,304 564,304" fill="none" stroke="var(--panel-light)" stroke-width="2"/>
    <polygon points="628,300 1080,300 1084,304 1084,672 1036,721 604,721 604,326"
             fill="var(--panel-fill)" stroke="var(--panel-edge)" stroke-width="5"/>
    <polyline points="630,304 1080,304" fill="none" stroke="var(--panel-light)" stroke-width="2"/>
  </svg>

  <ul class="panel-text objective-left">
    <li>Profit from inefficiencies in equity and index options markets
      <ul class="sub-list">
        <li>Buy options that are underpriced</li>
        <li>Sell options that are overpriced</li>
      </ul>
    </li>
  </ul>

  <ul class="panel-text objective-right">
    <li>Achieve outsized and consistent returns by maintaining a small and nimble fund that can exploit price inefficiencies and move in and out of trades quickly</li>
  </ul>
</main>
</body>
</html>
```